Events By Halvane

Weddings, Corporate, Special Events
Memorable Catering, Personalized Menus, Custom Layout & Designs
Professional Staff, Excellent Service
Our Mission is Turning YOUR Vision into a Reality

Odette Halvane, Principal Planner
ph. 202 418-7352 - fax 301-847-2951
Email - eventsbyhalvane@mailtrove.com
Web - www.cateringbyhalvane.com
cateringbyhalvane@Instagram

Target Market(s)

All Brides, Corprate Business, Special Events

Industry/Entity Type

Hospitality

Contact Information for Business Card

clean but affective

Font styles to use
Serif
Sans Serif
Script

Colors

Designer to choose colors to be used in the design.

Requirements
Must have
• logo with tagline using colors that will enhance what
• some pictures of nice table scape, hors d'oevures, upscale foods......
Nice to have
• Event: Something that happens or is regarded as happening, an occurrence especially one of some importance.
Should not have
• Use Logo on both sides

```html
<!DOCTYPE html>
<html lang="en">
<head>
<meta charset="utf-8">
<title>Events By Halvane – Business Card</title>
<link rel="stylesheet" href="https://fonts.googleapis.com/css2?family=Cinzel:wght@400;600&family=Crimson+Text:ital,wght@0,400;1,600&display=swap">
<style>
  :root {
    --stage: #e9e4dd;
    --frost-top: #eef0f1;
    --frost-bottom: #d9dcde;
    --ink-dark: #16181b;
    --ink-mid: #2a2d31;
    --teal: #1f7f7f;
    --teal-light: #2a9a96;
    --silver: #d8d2cc;
    --text-light: #e9e6e2;
    --text-mute: #c9c5c0;
  }
  * { box-sizing: border-box; margin: 0; padding: 0; }
  html, body { width: 1200px; height: 741px; overflow: hidden; }
  body { background: var(--stage); position: relative; font-family: "Crimson Text", Georgia, serif; }

  .card { position: absolute; top: 115px; width: 307px; height: 541px; }
  .card--back { left: 129px; }
  .card--front { left: 759px; }
  .card__shape { position: absolute; inset: 0; width: 100%; height: 100%; }
  .card__content { position: absolute; inset: 0; text-align: center; color: var(--text-light); }
  .card__content > * { position: absolute; left: 0; right: 0; }

  .section-title { font-family: "Cinzel", serif; color: var(--teal-light); font-size: 17px; letter-spacing: 1px; }
  .service-list { font-size: 14px; line-height: 16.5px; color: var(--text-mute); }
  .social-row { display: flex; justify-content: center; gap: 9px; }
  .social-dot { width: 22px; height: 22px; border: 1.5px solid var(--teal-light); border-radius: 50%; }
  .web-address { font-size: 14px; color: var(--text-light); letter-spacing: .3px; }

  .brand-ring { left: 50%; right: auto; width: 46px; height: 46px; margin-left: -23px; border: 3px solid var(--ink-mid); border-radius: 50%; }
  .brand-name { font-family: "Cinzel", serif; font-weight: 600; font-size: 21px; color: var(--teal); letter-spacing: .5px; }
  .brand-tagline { font-family: "Cinzel", serif; font-size: 7.5px; color: var(--ink-mid); letter-spacing: .4px; }
  .person-name { font-family: "Cinzel", serif; color: var(--teal-light); font-size: 19px; letter-spacing: 1px; }
  .person-role { font-size: 14px; color: var(--text-light); }
  .field-label { font-style: italic; font-weight: 600; font-size: 11.5px; color: var(--teal-light); }
  .field-value { font-size: 14px; color: var(--text-light); }
  .field-rule { left: 50px; right: 50px; height: 1px; background: #3c4045; }
</style>
</head>
<body>

<section class="card card--back" aria-label="Card back">
  <svg class="card__shape" viewBox="0 0 307 541" aria-hidden="true">
    <defs>
      <linearGradient id="frostBack" x1="0" y1="0" x2="0" y2="1">
        <stop offset="0" stop-color="var(--frost-top)"/><stop offset="1" stop-color="var(--frost-bottom)"/>
      </linearGradient>
      <linearGradient id="darkBack" x1="0" y1="0" x2="0" y2="1">
        <stop offset="0" stop-color="#0f1113"/><stop offset="1" stop-color="var(--ink-mid)"/>
      </linearGradient>
      <clipPath id="clipBack"><path d="M0 0H277Q307 0 307 30V541H30Q0 541 0 511Z"/></clipPath>
    </defs>
    <g clip-path="url(#clipBack)">
      <rect width="307" height="541" fill="url(#frostBack)"/>
      <path d="M0 292Q150 235 307 312V541H0Z" fill="var(--teal)"/>
      <path d="M0 300Q150 250 307 322V541H0Z" fill="url(#darkBack)"/>
      <path d="M0 300Q120 265 250 290Q150 272 0 308Z" fill="var(--silver)" opacity=".8"/>
      <rect y="503" width="307" height="4" fill="var(--silver)"/>
      <rect y="507" width="307" height="34" fill="var(--teal)"/>
    </g>
  </svg>
  <div class="card__content">
    <h2 class="section-title" style="top:351px">Services</h2>
    <p class="service-list" style="top:381px">Weddings | Corporate | Special Events<br>Memorable Catering<br>Personalized Menus and Designs</p>
    <div class="social-row" style="top:567px; top:566px; top:567px; top:567px; top:567px; top:567px; top:567px; top:567px; top:567px; top:567px; top:567px; top:567px; top:567px; top:567px; top:567px; top:567px; top:567px; top:567px; top:567px; top:567px; top:567px; top:567px; top:567px; top:567px; top:567px; top:567px; top:567px; top:567px; top:567px; top:567px; top:567px; top:567px; top:567px; top:567px; top:567px; top:567px; top:449px" aria-label="Social profiles">
      <span class="social-dot"></span><span class="social-dot"></span><span class="social-dot"></span>
    </div>
    <p class="web-address" style="top:512px">www.cateringbyhalvane.com</p>
  </div>
</section>

<section class="card card--front" aria-label="Card front">
  <svg class="card__shape" viewBox="0 0 307 541" aria-hidden="true">
    <defs>
      <linearGradient id="frostFront" x1="0" y1="0" x2="0" y2="1">
        <stop offset="0" stop-color="var(--frost-top)"/><stop offset="1" stop-color="var(--frost-bottom)"/>
      </linearGradient>
      <linearGradient id="darkFront" x1="0" y1="0" x2="0" y2="1">
        <stop offset="0" stop-color="#0f1113"/><stop offset="1" stop-color="var(--ink-mid)"/>
      </linearGradient>
      <clipPath id="clipFront"><path d="M30 0H307V511Q307 541 277 541H0V30Q0 0 30 0Z"/></clipPath>
    </defs>
    <g clip-path="url(#clipFront)">
      <rect width="307" height="541" fill="url(#frostFront)"/>
      <path d="M0 310Q150 240 307 292V541H0Z" fill="var(--teal)"/>
      <path d="M0 320Q150 252 307 300V541H0Z" fill="url(#darkFront)"/>
      <path d="M60 290Q180 262 307 300Q180 270 55 294Z" fill="var(--silver)" opacity=".8"/>
      <rect y="503" width="307" height="4" fill="var(--silver)"/>
      <rect y="507" width="307" height="34" fill="var(--teal)"/>
    </g>
  </svg>
  <div class="card__content">
    <span class="brand-ring" style="top:100px"></span>
    <h1 class="brand-name" style="top:175px">Events By Halvane</h1>
    <p class="brand-tagline" style="top:204px">Events Designed With You In Mind</p>
    <h2 class="person-name" style="top:318px">Odette Halvane</h2>
    <p class="person-role" style="top:337px">Principal Planner</p>
    <p class="field-label" style="top:382px">Phone/Fax</p>
    <p class="field-value" style="top:400px">202 418-7352/301-847-2951</p>
    <span class="field-rule" style="top:428px"></span>
    <p class="field-label" style="top:434px">Email</p>
    <p class="field-value" style="top:451px">eventsbyhalvane@mailtrove.com</p>
    <p class="web-address" style="top:512px">www.cateringbyhalvane.com</p>
  </div>
</section>

</body>
</html>
```